Online-Marketing-Material für Reinigungsunternehmen
Zielgruppe
Wir sind ein seit Jahresanfang bestehende Reinigungsunternehmen.
Unsere Schwerpunkte liegen auf Treppenhausreinigung und Büroreinigung.
Die Anzeige soll auf Facebook / Instagram als Werbung angezeigt werden.
Kunden sind sowohl Unternehmer sowie auch Privathaushalte und Hausverwaltungen.
www.kolvaputz.de
Aufgabenstellung
Es darf gerne Modern und verspielt sein. Es soll und darf nicht billig wirken.
Wir haben auch ein Maskottchen. Es muss aber nicht auf die Anzeige mit drauf!

```html
<!DOCTYPE html>
<html lang="de">
<head>
<meta charset="utf-8">
<title>Kolva Putz – Anzeige</title>
<link rel="stylesheet" href="https://fonts.googleapis.com/css2?family=Poppins:wght@500;600;700;800&display=swap">
<style>
  :root {
    --photo-light: #a9dde9;
    --photo-mid: #7ccfdc;
    --photo-deep: #5fc0cf;
    --band-blue: #3c5eae;
    --band-blue-deep: #2f5fa9;
    --service-teal: #46b9ad;
    --footer-blue: #468bc8;
    --button-text: #3a6bb8;
    --arrow-green: #6cb52d;
    --white: #ffffff;
  }
  * { margin: 0; padding: 0; box-sizing: border-box; }
  html, body { width: 1200px; height: 1200px; overflow: hidden; background: var(--white); }
  body { font-family: "Poppins", sans-serif; color: var(--white); }
  .ad { position: relative; width: 1200px; height: 1200px; overflow: hidden; }

  .hero-photo {
    position: absolute; left: 0; top: 0; width: 1200px; height: 885px;
    background: linear-gradient(120deg, var(--photo-deep) 0%, var(--photo-mid) 45%, var(--photo-light) 100%);
  }
  .headline-band {
    position: absolute; left: 0; top: 0; width: 1200px; height: 885px;
    background: linear-gradient(180deg, var(--band-blue) 0%, var(--band-blue-deep) 100%);
    opacity: 0.95;
    clip-path: polygon(0 699px, 1200px 456px, 1200px 885px, 0 885px);
  }

  .brand { position: absolute; left: 99px; top: 128px; display: flex; align-items: flex-start; gap: 26px; }
  .brand-mark { width: 118px; height: 118px; background: var(--white); margin-top: 14px; flex: none; }
  .brand-name { font-weight: 700; font-size: 66px; line-height: 68px; color: var(--white); }
  .brand-owner { margin-top: 10px; font-weight: 500; font-size: 23px; color: var(--white); }

  .headline { position: absolute; left: 99px; top: 630px; font-weight: 800; }
  .headline-top { font-size: 67px; line-height: 76px; letter-spacing: 1.2px; }
  .headline-main { font-size: 127px; line-height: 128px; letter-spacing: 1px; margin-top: -2px; }

  .services {
    position: absolute; left: 0; top: 885px; width: 1200px; height: 112px;
    background: var(--service-teal);
    display: flex; align-items: center; padding-left: 98px; gap: 46px;
  }
  .service { display: flex; align-items: center; gap: 18px; font-weight: 600; font-size: 45px; line-height: 1; }
  .service svg { width: 32px; height: 26px; }

  .footer {
    position: absolute; left: 0; top: 997px; width: 1200px; height: 203px;
    background: var(--footer-blue);
  }
  .footer-text { position: absolute; left: 98px; top: 54px; font-weight: 500; font-size: 32px; line-height: 49px; }
  .cta {
    position: absolute; left: 871px; top: 66px; width: 231px; height: 72px;
    background: var(--white); border-radius: 8px;
    display: flex; align-items: center; justify-content: center; gap: 12px;
    color: var(--button-text); font-weight: 700; font-size: 31px; text-decoration: none;
  }
  .cta svg { width: 22px; height: 26px; }
</style>
</head>
<body>
<div class="ad">
  <div class="hero-photo" role="img" aria-label="Foto: gut gelaunte Reinigungskraft mit Lockenwicklern, Sonnenbrille und Handschuhen hält einen türkisen Besen vor hellblauem Hintergrund"></div>
  <div class="headline-band"></div>

  <div class="brand">
    <div class="brand-mark"></div>
    <div>
      <div class="brand-name">Kolva<br>Putz</div>
      <div class="brand-owner">Inh. Jonas Wereldt</div>
    </div>
  </div>

  <h1 class="headline">
    <div class="headline-top">SCHENKEN SIE IHREM OBJEKT</div>
    <div class="headline-main">NEUEN GLANZ</div>
  </h1>

  <div class="services">
    <div class="service">
      <svg viewBox="0 0 32 26"><path d="M3 13 L12 22 L29 4" fill="none" stroke="#fff" stroke-width="5" stroke-linecap="round" stroke-linejoin="round"/></svg>
      Treppenhausreinigung
    </div>
    <div class="service">
      <svg viewBox="0 0 32 26"><path d="M3 13 L12 22 L29 4" fill="none" stroke="#fff" stroke-width="5" stroke-linecap="round" stroke-linejoin="round"/></svg>
      Büroreinigung
    </div>
  </div>

  <div class="footer">
    <p class="footer-text">Zuverlässige, professionelle Reinigungskräfte<br>in den Kreisen Paderborn &amp; Gütersloh</p>
    <a class="cta" href="#">Anfragen
      <svg viewBox="0 0 22 26"><path d="M3 2 L11 2 L20 13 L11 24 L3 24 L12 13 Z" fill="var(--arrow-green)"/></svg>
    </a>
  </div>
</div>
</body>
</html>
```